HiItsJonBrell.com needs a modern, eye-catching business card design

My name is Jon Brell and I own a video training (software development industry) website. I need a business card design that is eye catching for when I travel to conferences or do seminars. I would prefer something simple but bold. Something along the lines of this: https://pixvaultstatic.example/gallery_img/530172/44018/44018_9917302_530172_image.jpg

Note that I do not have a specific logo, but I do have an caricature I use on my site of myself. I've not attached it because I'm not really a fan of having it on my business cards. I would prefer lettering instead of an image. You can go to my website (https://hiitsjonbrell.com) for inspiration.

I want to add the following information on my card (the order of these, their size, and their casing is up to you):

Jon Brell
jon@HiItsJonBrell.com
@HiItsJonBrell
HiItsJonBrell.com
vidsharehub.example/HiItsJonBrell

I would also like to have somewhere on the card a small ad that says "Get a free course at https://HiItsJonBrell.com/FreeCourse". Feel free to play with that wording or layout if you need. I would prefer this text to be at the bottom of the card and subtle. Some small eye-catching thing might be ok but nothing huge or garish.

I plan on printing this card at pressquill.example (https://www.pressquill.example/us/design-guidelines/business-cards.html). I would like it to be the standard size (3.66" x 2.16"). I would prefer rounded corners and horizontal orientation. This is a two-side design. I would prefer the side with all of the information be primarily white but I like color text (again, flexible on that). On the front side, I like simple. Maybe just HiItsJonBrell.com (casing on that is up to you - whatever looks and reads the best - that goes for all of the casing). As for font choices, I prefer a modern, clean font. For example, Open Sans Light can be a nice option.

Website Info (might be helpful for the card):
Color Palette

Darkest blue - #263246
Alternate blue - #2F4E6A
Light blue - #2A98C3
Orange - #FF6201
White - #FFFFFF

Font for Jon Brell Logo

Jellyka Estryas Handwriting
http://www.typecrate.example/jellyka_estryas_handwriting.font

Fonts for Site Content and VidShare Thumbnails

Lovelo (bold title font)
http://www.glyphmill.example/lovelo-font/

Open Sans (body font)
http://www.letterbarn.example/fonts/open-sans

Industry/Entity Type

Software Development

Contact Information for Business Card

Jon Brell
jon@HiItsJonBrell.com
@HiItsJonBrell
HiItsJonBrell.com
vidsharehub.example/HiItsJonBrell

Get a free course at https://HiItsJonBrell.com/FreeCourse

Colors

Designer to choose colors to be used in the design.

Requirements
Nice to have
• Modern color - maybe primarily a color on the front and then that color as an accent on the back.
Should not have
• Lots of colors - I LOVE color but do not want a rainbow of colors on the card.

```html
<!DOCTYPE html>
<html lang="en">
<head>
<meta charset="utf-8">
<title>HiItsJonBrell.com Business Card</title>
<link href="https://fonts.googleapis.com/css2?family=Open+Sans:wght@300;400;600&display=swap" rel="stylesheet">
<style>
  :root {
    --navy: #223147;
    --paper: #eceef3;
    --white: #f8f8fa;
    --accent: #2a98c3;
    --muted: #8a909c;
    --stage: #d3d3df;
  }
  * { box-sizing: border-box; margin: 0; padding: 0; }
  html, body { width: 1200px; height: 900px; overflow: hidden; }
  body {
    background: var(--stage);
    font-family: "Open Sans", Arial, sans-serif;
    position: relative;
  }
  .card {
    position: absolute;
    left: 270px;
    width: 660px;
    height: 390px;
    border-radius: 14px;
    overflow: hidden;
    box-shadow: 0 6px 18px rgba(40, 45, 70, 0.18);
  }
  .card--front { top: 40px; background: var(--navy); }
  .card--back { top: 470px; background: var(--paper); }

  /* Front */
  .front-brand {
    position: absolute;
    top: 112px; left: 0; right: 0;
    display: flex; align-items: center; justify-content: center;
    gap: 14px;
  }
  .portrait-slot {
    width: 74px; height: 84px;
    border-radius: 38px 38px 10px 10px;
    background: linear-gradient(180deg, #c58a66 0%, #2f5c73 100%);
  }
  .front-name {
    color: #ffffff;
    font-weight: 300;
    font-size: 46px;
    letter-spacing: 1px;
  }
  .front-ad-band {
    position: absolute;
    left: 0; right: 0; top: 294px; height: 52px;
    background: var(--white);
    display: flex; align-items: center; justify-content: center;
  }
  .front-ad-band p {
    color: var(--muted);
    font-size: 15px;
    font-weight: 400;
  }

  /* Back */
  .domain-band {
    position: absolute;
    left: 0; right: 0; top: 36px; height: 86px;
    background: var(--navy);
    display: flex; align-items: center; justify-content: center;
  }
  .domain-band h1 {
    color: #ffffff;
    font-weight: 400;
    font-size: 46px;
    letter-spacing: 0.5px;
  }
  .info {
    position: absolute;
    top: 136px; left: 0; right: 0; height: 136px;
  }
  .owner-name {
    position: absolute;
    left: 40px; top: 46px; width: 210px;
    text-align: center;
    color: var(--navy);
    font-weight: 600;
    font-size: 30px;
    white-space: nowrap;
  }
  .divider {
    position: absolute;
    left: 272px; top: 4px;
    width: 1.5px; height: 128px;
    background: var(--navy);
  }
  .contact-list {
    position: absolute;
    left: 296px; top: 6px;
    list-style: none;
  }
  .contact-list li {
    display: flex; align-items: center; gap: 10px;
    height: 31px;
    color: var(--navy);
    font-size: 17px;
    font-weight: 300;
    white-space: nowrap;
  }
  .contact-icon {
    width: 20px; height: 20px;
    border-radius: 2px;
    background: var(--accent);
    flex: none;
  }
  .ad-band {
    position: absolute;
    left: 0; right: 0; top: 282px; height: 70px;
    background: var(--navy);
    display: flex; align-items: center; justify-content: center;
  }
  .ad-band p {
    color: #b6bcc8;
    font-size: 16px;
    font-weight: 300;
  }
</style>
</head>
<body>

<section class="card card--front" aria-label="Card front">
  <div class="front-brand">
    <div class="portrait-slot" role="img" aria-label="Caricature portrait of Jon Brell"></div>
    <span class="front-name">Jon Brell</span>
  </div>
  <div class="front-ad-band">
    <p>Get a free course at https://HiItsJonBrell.com/FreeCourse</p>
  </div>
</section>

<section class="card card--back" aria-label="Card back">
  <div class="domain-band">
    <h1>HiItsJonBrell.com</h1>
  </div>
  <div class="info">
    <p class="owner-name">Jon Brell</p>
    <div class="divider"></div>
    <ul class="contact-list">
      <li>
        <svg class="contact-icon" viewBox="0 0 20 20" aria-hidden="true">
          <rect width="20" height="20" fill="#2a98c3"/>
          <rect x="4" y="6" width="12" height="8" fill="none" stroke="#fff" stroke-width="1.2"/>
          <polyline points="4,6 10,11 16,6" fill="none" stroke="#fff" stroke-width="1.2"/>
        </svg>
        jon@HiItsJonBrell.com
      </li>
      <li>
        <svg class="contact-icon" viewBox="0 0 20 20" aria-hidden="true">
          <rect width="20" height="20" fill="#2a98c3"/>
          <circle cx="10" cy="10" r="6" fill="none" stroke="#fff" stroke-width="1.2"/>
          <ellipse cx="10" cy="10" rx="2.6" ry="6" fill="none" stroke="#fff" stroke-width="1"/>
          <line x1="4" y1="10" x2="16" y2="10" stroke="#fff" stroke-width="1"/>
        </svg>
        HiItsJonBrell.com
      </li>
      <li><span class="contact-icon"></span>vidsharehub.example/HiItsJonBrell</li>
      <li><span class="contact-icon"></span>@HiItsJonBrell</li>
    </ul>
  </div>
  <div class="ad-band">
    <p>Get a free course at https://HiItsJonBrell.com/FreeCourse</p>
  </div>
</section>

</body>
</html>
```